Flyer design for Trail Beside Outback Trips

We need a new flyer for our tour business. Sketch hive produced a great flyer for us 4 years ago but it is time to update. We have had a price increase that needs to be reflected but we have noticed an issue with our current marketing.
Our tour is a "tagalong" tour which means you follow in your own vehicle. Unfortunately most people associate "tagalong" with 4wd (Four wheel drive vehicles). This is not the case for our tour which can be done in ANY type of vehicle. We need to get across at first glance that this tour is available to all vehicle types. We also need to stress that there is NOT MUCH DRIVING. We cover around 20km total of very easy driving. We go from point of interest to point of interest.
We want our customers to feel that this tour will be a better option than selecting a bus type tour because they use their own vehicle. Our option is also MUCH cheaper than bus options but provides a premium product. It's "cheap" but not cheap if you understand.
I will upload our previous flyer so you have an idea of what we do and how we have been presenting it. We are currently single sided DL but do not mind if we go into double sided DL if you feel that will enable you to share more information. Our price is $50 and half price for kids (as per old flyer)
Some things to remember when trying to appeal to our customer:
Choose a design that clearly communicates that our tagalong tour is suitable for all types of vehicles. For example, "Vehicle-Friendly Tagalong Tour" or "All-Vehicle Tagalong Tour".
Use clear language: Avoid using terms like "off-road" or "4x4" that may imply that our tour is only suitable for certain types of vehicles. Instead, use language that is inclusive and clearly communicates that all vehicles are welcome.
Include photos and videos of a variety of vehicles: This will show potential customers that our tagalong tour is not limited to four-wheel drive vehicles and that any type of vehicle can participate.
Highlight the benefits of a tagalong tour over a bus tour: Emphasise the flexibility and freedom that a tagalong tour offers, as well as the opportunity to explore off-the-beaten-path destinations that are not accessible by bus.
By incorporating these elements into your product presentation, you can avoid confusion and clearly communicate that our tagalong tour is suitable for any type of vehicle, while also highlighting the unique benefits of this type of tour.
Along with the emphasis on all vehicles you need to be clear about what we offer on the tour.
- The excitement of an opal mine tour with an award winning guide and opal miner.
- The wonder of an underground home and discovering how people live in an underground environment.
- Driving through the opal mining area for a close up view of the field.
- Our EXCLUSIVE opal cutting and polishing demonstration.
- The adventure of looking for your own opal.
For further information visit our web site "http://trailbeside.outbackway.example". Check our facebook page "https://www.facebook.com/trailbesideoutbacktrips". Search Seekora for "Coober Pedy", Trail beside Outback Coober Pedy" or "Coober Pedy Opal mining" to source images of our town and opals.
PLEASE ALSO FIND SOMEWHERE TO SAY "FREE UNPOWERED CAMPING AT TALMO'S WITH ALL TOURS AS WELL AS DISCOUNTS ON POWERED CAMPING" and make this stand out somehow. (http://stay-belowgrid.example.au)

Target Market(s)

18 to 80

Industry/Entity Type

Tourism

Font styles to use
Serif

Colors

Designer to choose colors to be used in the design.

Requirements
Must have
• Eye catching images and attention grabbing headlines
Nice to have
• Modern design.
Should not have
• References to 4wd or buses.

```html
<!DOCTYPE html>
<html lang="en">
<head>
<meta charset="utf-8">
<title>Trail Beside Outback Trips – DL Flyer</title>
<link rel="stylesheet" href="https://fonts.googleapis.com/css2?family=Montserrat:wght@300;400;500;600;700;800&family=Cormorant+SC:wght@500&display=swap">
<style>
  :root {
    --stage: #d3d3d3;
    --panel-dark: #2d2d2d;
    --panel-deep: #262626;
    --orange: #f5820c;
    --orange-soft: #f79a2e;
    --band-brown: #6e4a1f;
    --white: #ffffff;
    --rule: #8a6a46;
    --label: #1c1c1c;
  }
  * { box-sizing: border-box; margin: 0; padding: 0; }
  html, body { width: 900px; height: 1200px; overflow: hidden; }
  body {
    position: relative;
    background: var(--stage);
    font-family: "Montserrat", Arial, sans-serif;
    color: var(--white);
  }
  .flyer {
    position: absolute;
    width: 392px;
    height: 830px;
    overflow: hidden;
    background: linear-gradient(180deg, var(--panel-dark) 55%, #4a3a28 100%);
    box-shadow: 0 2px 8px rgba(0,0,0,.25);
  }
  .flyer--front { left: 45px; top: 230px; }
  .flyer--back { left: 472px; top: 68px; height: 832px; background: var(--panel-dark); }
  .flyer__art { position: absolute; left: 0; top: 0; }
  .side-label {
    position: absolute;
    font-family: "Cormorant SC", Georgia, serif;
    font-weight: 500;
    font-size: 40px;
    color: var(--label);
    letter-spacing: 1px;
  }
  .side-label--front { left: 180px; top: 1090px; }
  .side-label--back { left: 622px; top: 930px; }

  /* brand badge */
  .brand-badge {
    position: absolute; left: 15px; top: 233px;
    width: 166px; height: 166px; border-radius: 50%;
    background: var(--orange);
    box-shadow: 0 0 0 2px rgba(255,255,255,.15);
    display: flex; flex-direction: column; align-items: center; justify-content: center;
    text-align: center;
  }
  .brand-badge__name {
    font-weight: 600; font-size: 19px; line-height: 1.15; color: var(--white);
    width: 130px;
  }

  .tour-title { position: absolute; left: 0; right: 0; top: 407px; text-align: center; color: var(--orange); }
  .tour-title__lead { display: block; font-weight: 400; font-size: 31px; letter-spacing: .5px; line-height: 34px; }
  .tour-title__main { display: block; font-weight: 700; font-size: 30px; line-height: 34px; }
  .rule { position: absolute; height: 1px; background: var(--white); }
  .rule--orange { background: var(--orange); opacity: .8; }
  .tour-lede {
    position: absolute; left: 20px; right: 20px; top: 493px;
    text-align: center; color: var(--orange-soft); font-size: 14px; line-height: 18px; font-weight: 500;
  }
  .tour-body {
    position: absolute; left: 25px; right: 25px; top: 560px;
    text-align: center; font-size: 10.6px; line-height: 14px; font-weight: 400;
  }
  .tour-body p + p { margin-top: 12px; }
  .pill {
    position: absolute; background: var(--orange); color: var(--panel-deep);
    font-weight: 700; display: flex; align-items: center; justify-content: center; text-align: center;
    border-radius: 16px;
  }
  .pill--drive { left: 85px; top: 695px; width: 222px; height: 32px; font-size: 15px; }

  .info-band {
    position: absolute; left: 0; right: 0; height: 32px;
    background: var(--band-brown);
    display: flex; align-items: center;
  }
  .info-band--front { top: 773px; }
  .info-band--back { top: 772px; }
  .info-band__label {
    width: 110px; text-align: center; font-size: 9px; line-height: 11px; font-weight: 400;
    border-right: 1px solid var(--white);
  }
  .info-band__label strong { font-weight: 700; }
  .info-band__url { flex: 1; text-align: center; font-size: 12.5px; font-weight: 700; letter-spacing: .1px; }

  /* back */
  .price-badge {
    position: absolute; left: 218px; top: 168px; width: 150px; height: 150px; border-radius: 50%;
    background: var(--orange); color: var(--panel-deep);
    box-shadow: 0 0 0 3px rgba(0,0,0,.25);
    display: flex; flex-direction: column; align-items: center; justify-content: center; text-align: center;
  }
  .price-badge__amount { font-weight: 600; font-size: 48px; line-height: 46px; letter-spacing: -1px; font-stretch: condensed; }
  .price-badge__unit { font-weight: 600; font-size: 13px; border-bottom: 1px solid var(--panel-deep); padding-bottom: 2px; margin-bottom: 3px; }
  .price-badge__note { font-size: 7.5px; line-height: 9px; }
  .price-badge__note strong { font-weight: 700; }

  .pitch {
    position: absolute; left: 10px; right: 10px; top: 330px; text-align: center;
    color: var(--orange-soft); font-size: 17.5px; line-height: 24px; font-weight: 400;
  }
  .pitch strong { font-weight: 700; }
  .offer-tag {
    position: absolute; left: 0; top: 457px; width: 119px; height: 26px;
    background: var(--orange); color: var(--panel-deep);
    border-radius: 0 13px 13px 0; font-weight: 700; font-size: 13.5px;
    display: flex; align-items: center; justify-content: center;
  }
  .offer-list { position: absolute; left: 22px; right: 20px; top: 505px; list-style: none; }
  .offer-list li { position: relative; padding-left: 17px; font-size: 10.6px; line-height: 13px; margin-bottom: 14px; }
  .offer-list li::before {
    content: ""; position: absolute; left: 0; top: 4px; width: 6px; height: 6px; border-radius: 50%; background: var(--orange);
  }
  .pill--camp {
    left: 21px; top: 707px; width: 352px; height: 33px; flex-direction: column;
    font-size: 10.5px; line-height: 12px; font-weight: 700;
  }
  .pill--camp small { font-size: 8.6px; font-weight: 600; }
</style>
</head>
<body>

<section class="flyer flyer--front" aria-label="Flyer front">
  <svg class="flyer__art" width="392" height="830" viewBox="0 0 392 830">
    <defs>
      <linearGradient id="mineSky" x1="0" y1="0" x2="0" y2="1">
        <stop offset="0" stop-color="#a9b7c2"/>
        <stop offset=".45" stop-color="#c9c3bb"/>
        <stop offset=".7" stop-color="#a86a44"/>
        <stop offset="1" stop-color="#8a6048"/>
      </linearGradient>
    </defs>
    <circle cx="230" cy="540" r="250" fill="none" stroke="#3a3632" stroke-width="40" opacity=".5"/>
    <path role="img" aria-label="Photo: old rusted mining truck among opal field mullock heaps" d="M0 0H392V178C330 262 190 302 0 300Z" fill="url(#mineSky)"/>
    <path d="M0 300C190 302 330 262 392 178V196C330 282 190 318 0 314Z" fill="#e8e8e8"/>
    <path d="M0 314C190 318 330 282 392 196V232C320 312 180 340 0 336Z" fill="var(--orange)"/>
  </svg>

  <div class="brand-badge">
    <span class="brand-badge__name">Trail Beside Outback</span>
  </div>

  <h1 class="tour-title">
    <span class="tour-title__lead">ALL-VEHICLE</span>
    <span class="tour-title__main">TAGALONG TOUR</span>
  </h1>
  <div class="rule" style="left:31px;width:330px;top:483px"></div>
  <p class="tour-lede">Enjoy the 20 km total of very easy driving tour from the comfort of your own car</p>
  <div class="rule rule--orange" style="left:60px;width:272px;top:544px"></div>
  <div class="tour-body">
    <p>Our tour is a "tagalong" tour which means you follow in your own vehicle and not just with 4wd (four wheel drive vehicles) but in ANY type of vehicle you own.</p>
    <p>A unique tag-along journey throught Coober Pedy. Enjoy the tour as our guide takes you through a "Day in the life" of a Coober Pedy miner.</p>
  </div>
  <div class="rule rule--orange" style="left:60px;width:272px;top:670px"></div>
  <div class="pill pill--drive">NOT MUCH DRIVING</div>

  <div class="info-band info-band--front">
    <div class="info-band__label">FOR MORE<br><strong>INFORMATION</strong></div>
    <div class="info-band__url">www.trailbeside.outbackway.example</div>
  </div>
</section>

<section class="flyer flyer--back" aria-label="Flyer back">
  <svg class="flyer__art" width="392" height="832" viewBox="0 0 392 832">
    <defs>
      <linearGradient id="fieldGround" x1="0" y1="0" x2="0" y2="1">
        <stop offset="0" stop-color="#b07a63"/>
        <stop offset="1" stop-color="#c7a08a"/>
      </linearGradient>
    </defs>
    <circle cx="160" cy="520" r="220" fill="none" stroke="#363330" stroke-width="40" opacity=".5"/>
    <path role="img" aria-label="Photo: a guide showing two young children an opal find on the rocky field" d="M0 0H392V228C300 250 120 230 0 118Z" fill="url(#fieldGround)"/>
    <path d="M0 118C120 230 300 250 392 228V240C300 264 110 246 0 138Z" fill="#e8e8e8"/>
    <path d="M0 138C110 246 300 264 392 240V262C290 292 100 276 0 175Z" fill="var(--orange)"/>
  </svg>

  <div class="price-badge">
    <span class="price-badge__amount">$50</span>
    <span class="price-badge__unit">PER PERSON</span>
    <span class="price-badge__note">half price for kids &amp;<br><strong>Free</strong> for under 5 yrs</span>
  </div>

  <p class="pitch">Grab the opportunity to explore <strong>off-the-beaten-path destinations</strong> that are not accessible by bus and at much cheaper price</p>
  <div class="rule rule--orange" style="left:60px;width:272px;top:436px"></div>

  <div class="offer-tag">WE OFFER</div>
  <ul class="offer-list">
    <li>The excitement of an opal mine tour with an award winning guide and opal miner.</li>
    <li>The wonder of an underground home and discovering how people live in an underground environment.</li>
    <li>Driving through the opal mining area for a close up view of the field.</li>
    <li>Our EXCLUSIVE opal cutting and polishing demonstration.</li>
    <li>The adventure of looking for your own opal.</li>
  </ul>
  <div class="rule rule--orange" style="left:60px;width:272px;top:682px"></div>

  <div class="pill pill--camp">FREE UNPOWERED CAMPING AT TALMO'S<small>WITH ALL TOURS AS WELL AS DISCOUNTS ON POWERED CAMPING</small></div>

  <div class="info-band info-band--back">
    <div class="info-band__label">FOR MORE<br><strong>INFORMATION</strong></div>
    <div class="info-band__url">www.trailbeside.outbackway.example</div>
  </div>
</section>

<div class="side-label side-label--front">Front</div>
<div class="side-label side-label--back">Back</div>

</body>
</html>
```